Pagebook Ads for HOA Law Firm

We need to create certain ads for a Pagebook ads campaign. We are a law firm in Florida that represents homeowners against HOAs. We need to create the following ads:

1. Image Ads Specifications:

File Type: JPG or PNG
Ratio: 1.91:1 to 4:5
Resolution:
a) 1:1 ratio: 1080 x 1080 pixels
b) 4:5 ratio: 1080 x 1350 pixels
Maximum File Size: 30MB
Minimum Width: 600 pixels
Minimum Height:
a) 1:1 ratio: 600 pixels
b) 4:5 ratio: 750 pixels
Key Elements to Include in the Ads:

1) Headline: "HOA Violating Your Rights?"
2) Main Message: "We sue HOAs for Homeowners."
3) Firm Name: Lindqvist Harrow, P.A.
4) Website: www.covenantshieldcounsel.example
5) Phone Number: 1-800-555-0148
6) Florida Bar Compliance Statement: "Serving Homeowners in Florida with our main office in Miami-Dade."
7) Call-to-Action (CTA): Include a strong CTA such as “Contact us today for a consultation!”
8) Tone and Style: Professional yet approachable. The ad should emphasize trust, expertise, and our dedication to homeowners' rights.
9) Branding: Please use our firm's brand colors and fonts. Ensure that our logo is prominently placed within the ad.
10) Image Suggestions: Consider using images of Florida homes, frustrated homeowners, or visuals that evoke trust, protection, and legal authority.

```html
<!DOCTYPE html>
<html lang="en">
<head>
<meta charset="utf-8">
<title>Lindqvist Harrow, P.A. – HOA Ad</title>
<link rel="stylesheet" href="https://fonts.googleapis.com/css2?family=Poppins:wght@700&family=Roboto:wght@400;700&family=Roboto+Condensed:wght@700&family=Oswald:wght@600&display=swap">
<style>
  :root {
    --navy: #10148a;
    --orange: #fd8408;
    --white: #ffffff;
    --mist: #dedcd6;
  }
  * { margin: 0; padding: 0; box-sizing: border-box; }
  html, body { width: 1200px; height: 1200px; overflow: hidden; }
  body { background: var(--white); font-family: "Roboto", sans-serif; }
  .ad {
    position: relative; width: 1200px; height: 1200px; overflow: hidden;
    background: linear-gradient(180deg, var(--white) 0%, var(--white) 38%, var(--mist) 72%, #c9c8d0 80%, var(--navy) 92%, var(--navy) 100%);
  }
  .brand {
    position: absolute; top: 82px; left: 0; width: 1200px; text-align: center;
    font-family: "Roboto", sans-serif; font-weight: 700; font-size: 26px;
    color: var(--navy); letter-spacing: 1px;
  }
  .brand-dot {
    display: inline-block; width: 18px; height: 18px; border-radius: 50%;
    background: var(--navy); margin-right: 12px; vertical-align: -1px;
  }
  .headline {
    position: absolute; top: 210px; left: 0; width: 1200px; text-align: center;
    font-family: "Poppins", sans-serif; font-weight: 700; line-height: 110px;
  }
  .headline .line-1 { display: block; color: var(--orange); font-size: 118px; }
  .headline .line-2 { display: block; color: var(--navy); font-size: 118px; }
  .portrait { position: absolute; }
  .portrait-left {
    left: 0; top: 458px; width: 520px; height: 742px;
    background: linear-gradient(180deg, rgba(120,110,105,0.55) 0%, rgba(107,111,134,0.7) 40%, rgba(60,70,150,0.85) 75%, var(--navy) 100%);
    border-radius: 260px 260px 0 0 / 200px 200px 0 0;
  }
  .portrait-right {
    left: 690px; top: 490px; width: 510px; height: 710px;
    background: linear-gradient(180deg, rgba(200,160,140,0.5) 0%, rgba(35,51,122,0.8) 45%, var(--navy) 100%);
    border-radius: 255px 255px 0 0 / 200px 200px 0 0;
  }
  .compliance {
    position: absolute; top: 496px; left: 406px; width: 420px; text-align: center;
    font-size: 36px; line-height: 45px; color: var(--navy); font-weight: 400;
  }
  .badge {
    position: absolute; left: 492px; top: 795px; width: 230px; height: 230px;
    border-radius: 50%; background: var(--white);
    box-shadow: 0 0 0 10px rgba(255,255,255,0.35);
    text-align: center; font-family: "Oswald", sans-serif; font-weight: 600;
  }
  .badge::before {
    content: ""; position: absolute; inset: 7px; border-radius: 50%;
    border: 2px dotted var(--navy);
  }
  .badge span { position: absolute; left: 0; width: 100%; display: block; text-align: center; }
  .badge .b1 { top: 58px; font-size: 44px; line-height: 48px; color: var(--navy); }
  .badge .b2 { top: 108px; font-size: 44px; line-height: 48px; color: var(--orange); }
  .badge .b3 { top: 156px; font-size: 29px; line-height: 32px; color: var(--navy); }
  .cta {
    position: absolute; left: 69px; top: 1003px; width: 1069px; height: 110px;
    border-radius: 55px; background: var(--orange);
  }
  .cta-label {
    position: absolute; left: 5px; top: 5px; width: 500px; height: 100px;
    border-radius: 50px; background: var(--white);
    font-family: "Roboto Condensed", sans-serif; font-weight: 700;
    color: var(--navy); font-size: 33px; line-height: 37px;
    padding: 14px 0 0 24px;
  }
  .cta-icon { position: absolute; left: 420px; top: 15px; }
  .cta-phone {
    position: absolute; left: 518px; top: 0; height: 110px; line-height: 108px;
    font-family: "Oswald", sans-serif; font-weight: 600; font-size: 78px;
    color: var(--white); letter-spacing: 1px;
  }
  .website {
    position: absolute; top: 1126px; left: 0; width: 1200px; text-align: center;
    font-size: 33px; color: var(--white);
  }
</style>
</head>
<body>
<main class="ad">
  <div class="brand"><span class="brand-dot"></span>Lindqvist Harrow, P.A.</div>

  <h1 class="headline">
    <span class="line-1">HOA VIOLATING</span>
    <span class="line-2">YOUR RIGHTS?</span>
  </h1>

  <div class="portrait portrait-left" role="img" aria-label="Portrait of a smiling attorney in a grey suit and blue tie"></div>
  <div class="portrait portrait-right" role="img" aria-label="Portrait of a smiling attorney in a navy suit and patterned tie"></div>

  <p class="compliance">Serving<br>Homeowners<br>in Florida with<br>our main office<br>in Miami-Dade.</p>

  <div class="badge">
    <span class="b1">WE SUE</span>
    <span class="b2">HOAS FOR</span>
    <span class="b3">HOMEOWNERS.</span>
  </div>

  <div class="cta">
    <div class="cta-label">
      CONTACT US TODAY<br>FOR A CONSULTATION!
      <svg class="cta-icon" width="70" height="70" viewBox="0 0 70 70" aria-hidden="true">
        <circle cx="35" cy="35" r="35" fill="#10148a"/>
        <path d="M24 18c2-1 4 0 5 2l3 6c1 2 0 3-1 4l-2 2c2 5 5 8 10 10l2-2c1-1 3-2 4-1l6 3c2 1 3 3 2 5l-2 4c-1 2-3 3-6 2-12-3-21-12-24-24-1-3 0-5 2-6z" fill="#fd8408"/>
      </svg>
    </div>
    <div class="cta-phone">1-800-555-0148</div>
  </div>

  <p class="website">www.covenantshieldcounsel.example</p>
</main>
</body>
</html>
```